dulvex presentation

I would like to improve the presentation of the PoweePoint. That attached.

Target Market(s)

Hotel sector - laboratories - industry

Font styles to use
Other font styles liked:
• como las del diseño

Requirements
Must have
• This PowerPoint. it has to serve as a company presentation.
Nice to have
• I wish it were pleasant to read. with background images or photographs that reinforce the text.

```html
<!DOCTYPE html>
<html lang="ca">
<head>
<meta charset="utf-8">
<title>dulvex – presentació d'empresa</title>
<link href="https://fonts.googleapis.com/css2?family=Open+Sans:wght@400;600;700&display=swap" rel="stylesheet">
<style>
:root{
  --navy:#2c3b5e;
  --blue:#2f4f9a;
  --red:#f0544f;
  --grey:#8b8b8b;
  --ink:#333;
  --bg:#ffffff;
}
*{box-sizing:border-box;margin:0;padding:0}
html,body{width:1200px;height:2504px;overflow:hidden;background:var(--bg);font-family:'Open Sans',Arial,sans-serif;color:var(--ink)}
.deck{position:relative;width:1200px;height:2504px}
.slide{position:absolute;width:550px;height:316px;overflow:hidden;background:#fff;box-shadow:0 0 0 1px #e3e3e3}
.col-a{left:20px}.col-b{left:630px}
.row1{top:10px}.row2{top:370px}.row3{top:730px}.row4{top:1090px}.row5{top:1450px}.row6{top:1810px}.row7{top:2170px}
.photo{position:absolute}
.full{inset:0}
.ph-work{background:
  radial-gradient(ellipse 40% 55% at 35% 60%,rgba(232,110,40,.95),rgba(232,110,40,0) 70%),
  radial-gradient(ellipse 35% 50% at 65% 45%,rgba(240,236,228,.9),rgba(240,236,228,0) 70%),
  linear-gradient(180deg,#9aa7b3 0%,#6f7b86 45%,#4b545c 100%)}
.ph-hotel{background:
  radial-gradient(ellipse 70% 40% at 50% 78%,rgba(60,48,38,.85),rgba(60,48,38,0) 75%),
  radial-gradient(ellipse 60% 45% at 50% 45%,rgba(232,214,186,.95),rgba(232,214,186,0) 75%),
  linear-gradient(180deg,#6f97c4 0%,#9db7d3 25%,#cdb796 55%,#6d5644 100%)}
.ph-rest{background:
  radial-gradient(ellipse 30% 35% at 70% 30%,rgba(255,226,170,.9),rgba(255,226,170,0) 70%),
  radial-gradient(ellipse 50% 40% at 40% 80%,rgba(20,16,12,.85),rgba(20,16,12,0) 75%),
  linear-gradient(135deg,#2e251d 0%,#6e5840 50%,#cdb48d 100%)}
.ph-office{background:
  radial-gradient(ellipse 45% 40% at 30% 30%,rgba(255,255,255,.95),rgba(255,255,255,0) 70%),
  radial-gradient(ellipse 40% 30% at 60% 80%,rgba(60,64,70,.8),rgba(60,64,70,0) 75%),
  linear-gradient(160deg,#e6e8ea 0%,#b6bcc2 55%,#7c838a 100%)}
.ph-shop{background:
  radial-gradient(ellipse 20% 60% at 15% 50%,rgba(15,15,15,.9),rgba(15,15,15,0) 75%),
  radial-gradient(ellipse 20% 60% at 85% 50%,rgba(15,15,15,.9),rgba(15,15,15,0) 75%),
  radial-gradient(ellipse 45% 30% at 50% 20%,rgba(250,246,236,.9),rgba(250,246,236,0) 75%),
  linear-gradient(180deg,#8f8a82 0%,#c9c1b4 50%,#5a5650 100%)}
.ph-room{background:
  radial-gradient(ellipse 45% 30% at 55% 70%,rgba(250,246,240,.95),rgba(250,246,240,0) 75%),
  radial-gradient(ellipse 30% 45% at 20% 40%,rgba(70,62,54,.85),rgba(70,62,54,0) 75%),
  linear-gradient(135deg,#5e554c 0%,#b9a893 50%,#ece4d8 100%)}
.ph-lab{background:
  radial-gradient(ellipse 40% 50% at 40% 50%,rgba(70,110,150,.8),rgba(70,110,150,0) 75%),
  linear-gradient(135deg,#8fb0c8,#e6eef3)}
.ph-ind{background:
  radial-gradient(ellipse 40% 50% at 60% 50%,rgba(40,50,60,.8),rgba(40,50,60,0) 75%),
  linear-gradient(135deg,#6e7f8d,#c2cbd2)}
.ph-city{background:
  radial-gradient(ellipse 60% 40% at 50% 70%,rgba(210,190,160,.95),rgba(210,190,160,0) 75%),
  linear-gradient(180deg,#7ea6d1 0%,#b3c9df 35%,#c2a987 65%,#705a46 100%)}
.brand{font-weight:700;letter-spacing:1px;color:var(--blue)}
.brand-mark{display:inline-block;width:12px;height:12px;background:var(--red);margin-left:6px;vertical-align:middle}

/* cover */
.cover .brand{position:absolute;left:318px;top:42px;font-size:38px}
.cover .rule{position:absolute;left:318px;top:100px;width:200px;height:3px;background:var(--red)}
.cover .edge{position:absolute;left:300px;top:0;width:4px;height:316px;background:var(--red)}
/* intro */
.intro h2{text-align:center;font-size:21px;font-weight:600;margin-top:22px;color:var(--navy)}
.intro .head-rule{width:100%;height:1px;background:#e2e2e2;margin-top:14px}
.intro ol{list-style:none;margin:18px 0 0 78px}
.intro li{display:flex;align-items:center;gap:18px;height:48px;font-size:12px}
.intro .n{font-size:28px;font-weight:600;width:44px}
.footer-brand{position:absolute;bottom:12px;left:0;right:0;text-align:center;font-size:12px}
/* areas */
.areas .brand{position:absolute;left:20px;top:12px;font-size:12px}
.areas .head-rule{position:absolute;left:0;right:0;top:40px;height:1px;background:#e2e2e2}
.areas h2{position:absolute;top:64px;width:100%;text-align:center;font-size:21px;font-weight:600;color:var(--navy)}
.areas .lead{position:absolute;top:114px;left:30px;right:30px;font-size:9px;text-align:center}
.areas .tiles{position:absolute;left:0;right:0;top:142px;height:110px;display:grid;grid-template-columns:repeat(4,1fr)}
.tile{position:relative;display:flex;align-items:flex-end;justify-content:center;padding-bottom:12px;color:#fff;font-size:9px;font-weight:700}
/* services */
.services .brand{position:absolute;left:20px;top:12px;font-size:12px}
.services h2{position:absolute;top:12px;width:100%;text-align:center;font-size:17px;font-weight:600;color:var(--navy)}
.services .lead{position:absolute;top:44px;left:20px;right:20px;font-size:8px}
.svc{position:absolute;left:20px;right:20px;height:56px;display:flex;gap:14px}
.svc .photo{position:relative;width:100px;height:56px;flex:none}
.svc h3{font-size:10px;font-weight:700;margin-top:4px}
.svc p{font-size:8px;margin-top:3px;line-height:1.3}
/* projects */
.box{position:absolute;display:flex;align-items:center;justify-content:center;text-align:center;color:#fff;font-size:20px;font-weight:600;line-height:1.3}
/* case */
.case .veil{position:absolute;inset:0;background:linear-gradient(180deg,rgba(44,59,94,.35),rgba(44,59,94,.7))}
.case h2{position:absolute;left:110px;top:112px;width:420px;font-size:27px;color:#fff;font-weight:600;line-height:1.2;text-align:center}
.case p{position:absolute;left:330px;top:220px;width:200px;color:#fff;font-size:8px;line-height:1.45}
/* info boxes */
.info{position:absolute;padding:14px 18px;color:#fff}
.info h3{font-size:10px;font-weight:700;margin-bottom:6px}
.info p{font-size:8px;line-height:1.5}
/* thanks */
.thanks .card{position:absolute;left:36px;top:36px;width:200px;height:244px;background:#fff;border:2px solid var(--red);padding:18px}
.thanks .tag{background:var(--navy);color:#fff;font-weight:700;font-size:17px;padding:6px 10px;display:inline-block}
.thanks h3{font-size:12px;margin:16px 0 8px;color:var(--navy)}
.thanks p{font-size:8px;line-height:1.7}
.thanks .brand{position:absolute;right:36px;top:130px;font-size:38px}
</style>
</head>
<body>
<main class="deck">

<section class="slide cover col-a row1">
  <div class="photo ph-work" style="left:0;top:0;width:300px;height:316px" role="img" aria-label="Tècnics amb casc revisant una instal·lació"></div>
  <div class="edge"></div>
  <div class="brand">dulvex</div>
  <div class="rule"></div>
</section>

<section class="slide intro col-b row1">
  <h2>INTRODUCCIÓN</h2>
  <div class="head-rule"></div>
  <ol>
    <li><span class="n" style="color:var(--navy)">01</span>Les nostres principals àrees d'acció</li>
    <li><span class="n" style="color:var(--blue)">02</span>Quins serveis oferim als clients</li>
    <li><span class="n" style="color:var(--red)">03</span>Referències en 'Instal·lacions' destacades</li>
    <li><span class="n" style="color:var(--grey)">04</span>La satisfacció dels clients és la nostra raó de ser</li>
  </ol>
  <div class="footer-brand brand">dulvex</div>
</section>

<section class="slide areas col-a row2">
  <div class="brand">dulvex</div>
  <div class="head-rule"></div>
  <h2>ÀREES D'ACCIÓ</h2>
  <p class="lead">dulvex treballa amb sectors diversos oferint solucions a mida. <span style="color:var(--red)">Som el seu soci tècnic de confiança.</span></p>
  <div class="tiles">
    <div class="tile ph-city" style="box-shadow:inset 0 0 0 200px rgba(47,79,154,.45)" role="img" aria-label="Hotel i restaurant">HOTELS I RESTAURANTS</div>
    <div class="tile ph-ind" style="box-shadow:inset 0 0 0 200px rgba(47,79,154,.6)" role="img" aria-label="Nau industrial">INDÚSTRIA</div>
    <div class="tile ph-lab" style="box-shadow:inset 0 0 0 200px rgba(240,84,79,.65)" role="img" aria-label="Laboratori">LABORATORIS</div>
    <div class="tile ph-shop" style="box-shadow:inset 0 0 0 200px rgba(139,139,139,.5)" role="img" aria-label="Botiga">COMERÇOS</div>
  </div>
</section>

<section class="slide services col-b row2">
  <div class="brand">dulvex</div>
  <h2>SERVEIS</h2>
  <p class="lead">Oferim un servei integral, des del disseny fins al manteniment de cada instal·lació.</p>
  <div class="svc" style="top:64px"><div class="photo ph-lab" role="img" aria-label="Tècnic al laboratori"></div><div><h3 style="color:var(--blue)">LABORATORIS</h3><p>Instal·lacions de climatització i aire net per a espais controlats.</p></div></div>
  <div class="svc" style="top:126px"><div class="photo ph-hotel" role="img" aria-label="Interior d'hotel"></div><div><h3 style="color:var(--blue)">HOTELS I RESTAURACIÓ</h3><p>Projectes complets d'instal·lacions per a hotels i restaurants.</p></div></div>
  <div class="svc" style="top:188px"><div class="photo ph-ind" role="img" aria-label="Operari industrial"></div><div><h3 style="color:var(--red)">INDÚSTRIA</h3><p>Solucions eficients per a naus i processos.</p></div></div>
  <div class="svc" style="top:250px"><div class="photo ph-work" role="img" aria-label="Servei tècnic"></div><div><h3 style="color:var(--grey)">SERVEI POST-VENDA</h3><p>Manteniment preventiu i correctiu.</p></div></div>
</section>

<section class="slide col-a row3">
  <div class="photo ph-city full" role="img" aria-label="Façana de l'Hotel Vidal Mar"></div>
  <div class="box" style="left:18px;top:18px;width:170px;height:64px;background:var(--blue)">Hotel Vidal Mar<br>Barcelona</div>
</section>

<section class="slide col-b row3">
  <div class="photo ph-rest" style="left:0;top:0;width:24px;height:316px" role="img" aria-label="Detall del restaurant"></div>
  <div class="box" style="left:24px;top:0;width:122px;height:316px;background:#7b7b7b">Restaurant<br>Albera<br>Barcelona</div>
  <div class="photo ph-rest" style="left:146px;top:0;right:0;bottom:0" role="img" aria-label="Sala del Restaurant Albera"></div>
</section>

<section class="slide col-a row4">
  <div class="photo ph-office" style="left:0;top:0;width:550px;height:316px" role="img" aria-label="Oficina amb taula i cadires"></div>
  <div class="box" style="left:300px;top:0;width:250px;height:316px;background:var(--red)">Oficines<br>Norvent<br>Barcelona</div>
</section>

<section class="slide col-b row4">
  <div class="photo ph-shop full" role="img" aria-label="Interior de la botiga Lumira"></div>
  <div class="box" style="left:190px;top:76px;width:170px;height:164px;background:var(--navy)">Lumira<br>Barcelona</div>
</section>

<section class="slide col-a row5">
  <div class="photo ph-room" style="left:0;top:0;width:240px;height:316px" role="img" aria-label="Habitació de la residència"></div>
  <div class="photo ph-room" style="left:240px;top:0;right:0;bottom:0;filter:brightness(1.08)" role="img" aria-label="Llit i mobiliari de la residència"></div>
  <div class="box" style="left:250px;top:16px;width:240px;height:52px;background:#8a8a8a;font-size:15px">Residència La Plaça<br>Barcelona</div>
</section>

<section class="slide case col-b row5">
  <div class="photo ph-city full" role="img" aria-label="Façana de l'Hotel Sant Roc"></div>
  <div class="veil"></div>
  <h2>Hotel Sant Roc 5* GL Barcelona<br>Case Study</h2>
  <p>Reforma integral de les instal·lacions de climatització, ventilació i aigua calenta de l'hotel.</p>
</section>

<section class="slide col-a row6">
  <div class="info" style="left:0;top:0;width:275px;height:158px;background:var(--red)"><h3>ABAST DEL PROJECTE</h3><p>Substitució de la producció de fred i calor, renovació de climatitzadors i nova distribució d'aire a totes les plantes. Obra executada per fases sense tancar l'hotel i amb control continu.</p></div>
  <div class="photo ph-room" style="left:275px;top:0;width:275px;height:158px" role="img" aria-label="Habitació de l'hotel"></div>
  <div class="photo ph-city" style="left:0;top:158px;width:275px;height:158px" role="img" aria-label="Façana de l'hotel"></div>
  <div class="info" style="left:275px;top:158px;width:275px;height:158px;background:var(--red)"><h3>LOCALITZACIÓ</h3><p>Edifici històric al centre de Barcelona, amb 120 habitacions, restaurant, spa i terrassa.</p></div>
</section>

<section class="slide col-b row6">
  <div class="info" style="left:0;top:0;width:275px;height:158px;background:#5b6170"><h3>CONTEXT</h3><p>Els equips existents superaven la vida útil i generaven un consum elevat i queixes de confort.</p></div>
  <div class="info" style="left:275px;top:0;width:275px;height:158px;background:var(--red)"><h3>OBJECTIUS DEL CLIENT</h3><p>Reduir el consum energètic.<br>Millorar el confort.<br>Minimitzar l'impacte de l'obra.</p></div>
  <div class="info" style="left:0;top:158px;width:275px;height:158px;background:var(--navy)"><h3>CONTROL</h3><p>Nou sistema de gestió centralitzada amb supervisió remota.<br><br><b>COMMISSIONING I BMS</b><br>Posada en marxa i verificació de totes les instal·lacions.</p></div>
  <div class="info" style="left:275px;top:158px;width:275px;height:158px;background:var(--red)"><h3>CARACTERÍSTIQUES</h3><p>Bomba de calor d'alta eficiència.<br>Recuperació de calor.<br>Fan-coils de baix consum.</p></div>
</section>

<section class="slide thanks col-a row7">
  <div class="photo ph-work full" role="img" aria-label="Tècnics treballant en una instal·lació"></div>
  <div class="card">
    <span class="tag">THANK YOU</span>
    <h3>MOLTES GRÀCIES</h3>
    <p>Carrer del Molí, 24<br>08000 Barcelona<br>+34 900 000 000<br>info@dulvex.example</p>
  </div>
  <div class="brand">dulvex<span class="brand-mark"></span></div>
</section>

</main>
</body>
</html>
```